Lakeshore Clinical Allies Business Flyers

I am in need of a nice, professional brochure that I can leave behind with my clients. I have template built, but will need a new design that I can be proud of and that I can have the template to update and change down the road. I will want to reflect my medical distribution services in the form of Labs I partner with (Genetic Testing and Pathology) and Pharmacies I partner with for Topical solutions (creams for commercial and medicare) as well as worker's compensation. Finally, I have toxicology testing.

Target Market(s)

Medical clinics, physicians

Industry/Entity Type

Medical

Font styles to use
Other font styles liked:
• see brochure (Avenir Next) NOTE: Feel free to use another font if you think it is more elegant and/or a better option

Colors
000000
cbcbcb
f7f7f7

Requirements
Must have
• Focus on my brand (trusted partner) showcase the logo (carbon fiber look on all black areas) See the bottom right of the brochure I uploaded. On the inside, I want to feature my labs and pharmacy(s). I will send you the link to them so you can use items from their websites. We are focusing on PROFESSIONAL and TRUSTED service with strong partnerships with world class labs, etc.
• Focus on we handle all the billing and collection processes. All of our partners are chosen because they have your patient satisfaction in mind as a top priority. We are always on the "right side" of insurance and are HIPPA compliant and have a zero tolerance for non-compliance.
• What we do: Testing (Toxicology and Genetic Testing) Pharmacogenetics studies how genetic various impact the way our bodies respond to certain medications. By having detailed patient data, physicians can now practice precise, individualized, tailored treatment programs based on personal date of each patient.
Nice to have
• Note the importance of the "mirroring/reflection" in my logo on the "P" and the "carbon fiber" look and feel on the black "M". if you can build that into the look and feel of the brochure, it would help to "pop" the brand and my logo.
• Build the partner labs/pharmacy into the brochure for credibility. ( I would say some of our key partners and leave it opened ended like we have many more)
• Topical Solutions: www.curavexallies.example (innovation/innovative medicare and commercial insurance solutions
• www.brindlecaremed.example (workers comp solutions)
• Labs:
• www.zenthoraassaylabs.example
• www.pellucigenomics.example
• I will provide more content and verbiage if needed, but much of it you can get from the website. The key is that we do all the billing, we supply all the materials including paperwork, forms, collection kits and all shipping. We differentiate ourselves by taking all the cumbersome work away from the staff through automation and best practices, topped off by personal/customized service.
Should not have
• Cluttered and busy...not many colors that create confusion and/or attention span issues.

```html
<!DOCTYPE html>
<html lang="en">
<head>
<meta charset="utf-8">
<title>Lakeshore Clinical Allies – Brochure Inside Spread</title>
<link href="https://fonts.googleapis.com/css2?family=Mulish:ital,wght@0,400;0,500;0,600;0,700;1,400&display=swap" rel="stylesheet">
<style>
  :root {
    --backdrop: #a8aaad;
    --panel-light: #ededed;
    --panel-dark: #000000;
    --ink: #1a1a1a;
    --ink-soft: #333333;
    --paper-white: #ffffff;
    --silver: #cbcbcb;
    --carbon-a: #0d0d0d;
    --carbon-b: #3a3a3a;
  }
  * { box-sizing: border-box; margin: 0; padding: 0; }
  html, body { width: 1200px; height: 931px; overflow: hidden; }
  body {
    background: var(--backdrop);
    font-family: "Mulish", "Avenir Next", sans-serif;
    color: var(--ink);
    position: relative;
  }
  .spread {
    position: absolute; left: 52px; top: 38px;
    width: 1105px; height: 854px;
    display: flex;
  }
  .panel { position: relative; height: 100%; overflow: hidden; }
  .panel--what { width: 367px; background: var(--panel-light); }
  .panel--services { width: 369px; background: var(--panel-dark); color: var(--paper-white); }
  .panel--partner { width: 369px; background: var(--panel-light); }

  .carbon-band {
    position: absolute; left: 0; right: 0; bottom: 0; height: 22px;
    background: linear-gradient(180deg, var(--carbon-b) 0%, var(--carbon-a) 55%, #222 100%);
  }

  .photo { position: absolute; }
  .photo--lab { left: 0; top: 0; width: 100%; height: 120px;
    background: linear-gradient(120deg, #c9d3dc 0%, #8fa1b2 45%, #dfe5ea 100%); }
  .photo--pharmacy { left: 214px; top: 88px; width: 78px; height: 78px;
    background: linear-gradient(135deg, #e9eef2, #b9c6cf); border: 4px solid var(--paper-white);
    transform: rotate(-6deg); box-shadow: 0 2px 5px rgba(0,0,0,.25); }
  .photo--tools { left: 282px; top: 90px; width: 76px; height: 76px;
    background: linear-gradient(135deg, #dfe6ea, #9fb0bb); border: 4px solid var(--paper-white);
    transform: rotate(6deg); box-shadow: 0 2px 5px rgba(0,0,0,.25); }
  .photo--team { left: 0; top: 0; width: 100%; height: 185px;
    background: linear-gradient(160deg, #d5dde4 0%, #9aabb9 50%, #e5e9ed 100%); }
  .photo--insurance { left: 246px; top: 142px; width: 96px; height: 90px;
    background: linear-gradient(135deg, #f3f5f6, #b8c2c8); border: 4px solid var(--paper-white);
    transform: rotate(8deg); box-shadow: 0 2px 5px rgba(0,0,0,.25); }

  .panel-title { font-weight: 500; font-size: 22px; letter-spacing: .3px; position: absolute; }

  /* What we do */
  .what-title { left: 30px; top: 138px; }
  .offer { position: absolute; left: 26px; width: 322px; font-size: 12px; line-height: 15px; color: var(--ink-soft); }
  .offer-icon { float: left; width: 60px; height: 60px; border-radius: 50%; margin: 0 8px 2px 0; shape-outside: circle(50%); }
  .offer-icon--genetics { background: radial-gradient(circle at 40% 40%, #e6f1f7, #79a9c4); }
  .offer-icon--topicals { background: radial-gradient(circle at 40% 40%, #f0e2d6, #9a6c52); }
  .offer-icon--tox { background: radial-gradient(circle at 40% 40%, #d6e4f3, #c2262e 70%, #3f6fb0); }
  .offer h3 { font-size: 16.5px; font-weight: 600; line-height: 18px; color: var(--ink); margin-top: 4px; }
  .offer h4 { font-size: 13px; font-weight: 600; line-height: 16px; color: var(--ink); }
  .offer-sub { margin-top: 12px; }
  .offer--testing { top: 177px; }
  .offer--topicals { top: 431px; }
  .offer--tox { top: 653px; }

  /* Services */
  .services { position: absolute; left: 39px; top: 28px; width: 305px; font-size: 12.5px; line-height: 16.5px; }
  .services h2 { font-size: 22px; font-weight: 500; line-height: 26px; margin-bottom: 8px; }
  .services h3 { font-size: 16px; font-weight: 500; line-height: 20px; }
  .services .group + .group { margin-top: 11px; }
  .bullets { list-style: none; }
  .bullets > li { position: relative; padding-left: 15px; }
  .bullets > li::before { content: ""; position: absolute; left: 2px; top: 6px; width: 4.5px; height: 4.5px; border-radius: 50%; background: var(--paper-white); }
  .sub-bullets { list-style: none; }
  .sub-bullets li { position: relative; padding-left: 32px; }
  .sub-bullets li::before { content: "o"; position: absolute; left: 17px; top: 0; font-size: 11px; }
  .clients { position: absolute; left: 33px; top: 618px; width: 320px; font-size: 12.5px; line-height: 16.2px; }
  .clients h2 { font-size: 22px; font-weight: 500; line-height: 26px; margin-bottom: 6px; }
  .clients .bullets > li { padding-left: 21px; }
  .clients .bullets > li::before { left: 8px; }

  /* Partner */
  .partner-title { left: 20px; top: 210px; }
  .partner-block { position: absolute; left: 22px; width: 335px; font-size: 12px; line-height: 15px; color: var(--ink-soft); }
  .partner-block h3 { font-size: 15px; font-weight: 600; line-height: 18px; color: var(--ink); margin-bottom: 4px; }
  .partner-block--labs { top: 248px; }
  .partner-block--pharm { top: 443px; left: 25px; }
  .partner-names { position: absolute; left: 22px; width: 335px; display: flex; justify-content: space-between; align-items: center; }
  .partner-names--labs { top: 396px; }
  .partner-names--pharm { top: 570px; }
  .partner-name { font-size: 11px; font-weight: 600; color: var(--ink-soft); display: flex; align-items: center; gap: 5px; white-space: nowrap; }
  .partner-name .dot { width: 10px; height: 10px; border-radius: 50%; background: #4a4a4a; }

  .reference-title { left: 22px; top: 636px; }
  .reference-badge { position: absolute; left: 23px; top: 676px; width: 50px; height: 50px; border-radius: 50%; background: #d4d4d4; border: 2px solid #bdbdbd; }
  .reference-quote { position: absolute; left: 84px; top: 672px; width: 268px; font-size: 10.6px; line-height: 13.4px; color: var(--ink-soft); }
  .reference-quote cite { display: block; font-style: italic; }
</style>
</head>
<body>
<main class="spread">

  <section class="panel panel--what">
    <div class="photo photo--lab" role="img" aria-label="Photo of a scientist working in a laboratory"></div>
    <div class="photo photo--pharmacy" role="img" aria-label="Photo of pharmacy shelves"></div>
    <div class="photo photo--tools" role="img" aria-label="Photo of medical instruments"></div>
    <h2 class="panel-title what-title">WHAT WE DO:</h2>

    <article class="offer offer--testing">
      <div class="offer-icon offer-icon--genetics" role="img" aria-label="Photo of a pipette over test samples"></div>
      <h3>TESTING</h3>
      <h4>Genetics</h4>
      <p>Our testing partners help to empower every medical professional and patient with the specific knowledge to properly prescribe and dose a patient’s symptoms and conditions with accurate medication in specific dosages for optimized results. All of this can be done by providing genetic information specific to the patient and the condition to be treated.</p>
      <div class="offer-sub">
        <h4>Pathology</h4>
        <p>Our partner pathology laboratory is dedicated to bringing quality anatomic pathology services to Urologists, Gastroenterologists, Dermatologists, Neurologists, Pain Management Specialists and Podiatrists.</p>
      </div>
    </article>

    <article class="offer offer--topicals">
      <div class="offer-icon offer-icon--topicals" role="img" aria-label="Photo of topical cream on a fingertip"></div>
      <h3>TOPICALS</h3>
      <p>Our topically applied specialty products are manufactured, FDA-approved, and often covered by most insurance prescription plans. These products can be used to treat a variety of conditions including acute to chronic pain. We are also your partner for personalized medications that are made just for you! Like the professional physicians and providers we serve, we believe that a patient should be treated as a unique individual, and not as just another statistic and that the best-case scenario is when a patient, a medical provider, and a pharmacy work together to come up with the best possible treatment plan.</p>
    </article>

    <article class="offer offer--tox">
      <div class="offer-icon offer-icon--tox" role="img" aria-label="Photo of a sample collection tube"></div>
      <h3>TOXICOLOGY</h3>
      <p>Our labs offer comprehensive urine and saliva tox screening. Too often, because of the difficulty with monitoring and documenting patients’ compliance, many healthcare providers are reluctant to offer adequate pain management. Either the patients experience more discomfort that they would otherwise, or they are referred out to other practitioners who may not know their medical situations as well as their primary care provider.</p>
    </article>
    <div class="carbon-band"></div>
  </section>

  <section class="panel panel--services">
    <div class="services">
      <h2>OUR SERVICES:</h2>
      <div class="group">
        <h3>Genetic Testing</h3>
        <ul class="bullets">
          <li>Hereditary Cancer</li>
          <li>Inherited Conditions</li>
          <li>Pharmacogenetics (Drug Metabolism)</li>
          <li>Preconception &amp; Pregnancy</li>
        </ul>
      </div>
      <div class="group">
        <h3>Pathology</h3>
        <ul class="bullets">
          <li>Client Bill Programs</li>
          <li>Dermatology</li>
          <li>Epidermal Nerve Fiber Density (ENFD)</li>
          <li>Gastroenterology (General Biopsies)
            <ul class="sub-bullets">
              <li>Micro colitis</li>
              <li>EGD (Barrett’s, metaplasia, gastric carcinoma, celiac, etc.</li>
              <li>HER2/neu testing by IHC &amp; FISH for every gastric &amp; esophageal cancer</li>
              <li>Microsatellite instability testing for every colon cancer</li>
              <li>Special stand for H.pylori on every gastric biopsy</li>
            </ul>
          </li>
          <li>“Lean Lab” In-House Laboratory for Group Practice</li>
          <li>Podiatry
            <ul class="sub-bullets">
              <li>Biopsy and PAS (ie, histopathology)</li>
              <li>Skin Lesions/pigmented lesions/Nevi</li>
              <li>Plantar Warts</li>
              <li>Amputated toes</li>
              <li>Wound Debridement Tissue</li>
              <li>Soft Tissue Lesions/Tumors (neuroma)</li>
              <li>Bone Shaving</li>
              <li>Nail (Onychomycosis)</li>
            </ul>
          </li>
          <li>Urology
            <ul class="sub-bullets">
              <li>Prostate (needle core biopsies)</li>
            </ul>
          </li>
        </ul>
      </div>
    </div>

    <div class="clients">
      <h2>WHO WE SERVICE:</h2>
      <ul class="bullets">
        <li>Dermatology</li>
        <li>Family Practice</li>
        <li>Gastroenterology</li>
        <li>Mental Health</li>
        <li>Obstetrics and Gynecology</li>
        <li>Orthopedic and Sports Medicine</li>
        <li>Pain Management</li>
        <li>Physiatry</li>
        <li>Podiatry</li>
        <li>Urology</li>
      </ul>
    </div>
    <div class="carbon-band"></div>
  </section>

  <section class="panel panel--partner">
    <div class="photo photo--team" role="img" aria-label="Photo of a smiling team of medical professionals"></div>
    <div class="photo photo--insurance" role="img" aria-label="Photo of a health insurance form with a stethoscope"></div>
    <h2 class="panel-title partner-title">OUR PARTNER:</h2>

    <div class="partner-block partner-block--labs">
      <h3>Labs</h3>
      <p>All of our Lab Partners offer full spectrum testing and are CLIA certified and CAP accredited. We offer personalized support and paperless reporting via online portals and EMR integration. Most importantly, our lab employees care deeply for our patients and work tirelessly to deliver world class turnaround times and outstanding, easy to read and understand results.</p>
    </div>
    <div class="partner-names partner-names--labs">
      <span class="partner-name"><span class="dot"></span>Brightwell Rx</span>
      <span class="partner-name">Curavex Allies</span>
      <span class="partner-name">Brindlecare Med</span>
    </div>

    <div class="partner-block partner-block--pharm">
      <h3>Pharmacies</h3>
      <p>Lakeshore Clinical Allies bridges the gap between manufacturers and patients through our network of pharmacies that take care of everything for your valued patient from processing insurance, to ensuring delivery of the script straight to your patient's home.</p>
    </div>
    <div class="partner-names partner-names--pharm">
      <span class="partner-name"><span class="dot"></span>Pelluci Genomics</span>
      <span class="partner-name">Zenthora Assay Labs</span>
      <span class="partner-name">Corvane Pathology</span>
    </div>

    <h2 class="panel-title reference-title">REFERENCE</h2>
    <div class="reference-badge"></div>
    <blockquote class="reference-quote">
      <p>I have been working with Daniel and his team for over a year and we’ve been extremely impressed with his services and in particular, his attention to detail. Lakeshore Clinical Products and the labs and pharmacies they partner with provide our clinic great value and service. Our physicians and patients have been extremely satisfied with Daniel, especially his personal touch. We consider Daniel to be our partner and not just a vendor."</p>
      <cite>Marcus Hale, Riverbend Family Medical</cite>
    </blockquote>
    <div class="carbon-band"></div>
  </section>

</main>
</body>
</html>
```